Reef Lantern Tropical Fish Startup Design

I need professional business cards and social media profiles for our tropical fish shop.

Target Market(s)

Tropical fish enthusiasts

Industry/Entity Type

Tropical Fish

Font styles to use
Sans Serif
Script
Other font styles liked:
• Comforta

Colors
0054AA
0677BA
7BADD7
CADEEF
E8F1F8
0094D4
00A9DD
6FCCEA
C7EBF8
E9F6FB
00AB8E
00BBA5
67D7C9
C6EFE9
E9F9F6

Requirements
Must have
• fish, oceanic colors
Nice to have
• Lines, boxes, anything that groups the title to stand out
Should not have
• Any punctuations

```html
<!DOCTYPE html>
<html lang="en">
<head>
<meta charset="utf-8">
<title>Reef Lantern Business Cards</title>
<link rel="stylesheet" href="https://fonts.googleapis.com/css2?family=Montserrat:wght@700&family=Roboto:wght@400&display=swap">
<style>
  :root {
    --ocean-deep: #0054aa;
    --ocean-mid: #0677ba;
    --lagoon: #0094d4;
    --reef-teal: #00ab8e;
    --foam: #e9f6fb;
    --paper: #f5f7f8;
    --backdrop: #e6e7e9;
    --ink: #4a4a4a;
    --rule: #5a5a5a;
    --white: #ffffff;
  }
  * { margin: 0; padding: 0; box-sizing: border-box; }
  html, body { width: 1200px; height: 884px; overflow: hidden; }
  body {
    background: var(--backdrop);
    display: flex;
    align-items: center;
    justify-content: center;
    gap: 56px;
    font-family: "Roboto", sans-serif;
  }
  .card {
    width: 532px;
    height: 304px;
    position: relative;
    box-shadow: 0 6px 18px rgba(0,0,0,0.12);
    overflow: hidden;
  }

  .brand {
    display: flex;
    align-items: center;
    gap: 14px;
  }
  .brand-mark {
    flex: none;
    border-radius: 6px;
  }
  .wordmark {
    font-family: "Montserrat", sans-serif;
    font-weight: 700;
    text-transform: uppercase;
    letter-spacing: 2px;
    line-height: 1;
    white-space: nowrap;
  }

  /* Front */
  .card-front {
    background: linear-gradient(135deg, var(--ocean-deep) 0%, var(--ocean-mid) 100%);
    color: var(--white);
  }
  .card-front .brand {
    position: absolute;
    left: 50%;
    top: 104px;
    transform: translateX(-50%);
  }
  .card-front .brand-mark {
    width: 58px; height: 58px;
    background: linear-gradient(135deg, var(--lagoon), var(--reef-teal));
  }
  .card-front .wordmark { font-size: 42px; }
  .social-handle {
    position: absolute;
    right: 58px;
    top: 196px;
    display: flex;
    align-items: center;
    gap: 8px;
    font-size: 17px;
    letter-spacing: 0.3px;
  }
  .social-handle .dot {
    width: 16px; height: 16px;
    border-radius: 50%;
    background: var(--white);
  }

  /* Back */
  .card-back { background: var(--paper); }
  .card-back .brand {
    position: absolute;
    top: 40px;
    right: 56px;
  }
  .card-back .brand-mark {
    width: 46px; height: 46px;
    background: linear-gradient(135deg, var(--lagoon), var(--reef-teal));
  }
  .card-back .wordmark { font-size: 32px; color: var(--ocean-deep); }
  .divider {
    position: absolute;
    top: 150px;
    left: 254px;
    right: 24px;
    height: 1px;
    background: var(--rule);
  }
  .person {
    position: absolute;
    left: 34px;
    top: 140px;
  }
  .person-name {
    font-family: "Montserrat", sans-serif;
    font-weight: 700;
    font-size: 17px;
    color: var(--ocean-deep);
    text-transform: uppercase;
  }
  .person-role {
    font-size: 15px;
    color: var(--ink);
    margin-top: 2px;
  }
  .contact-list {
    list-style: none;
    margin-top: 10px;
  }
  .contact-list li {
    display: flex;
    align-items: center;
    gap: 9px;
    font-size: 15px;
    color: var(--ink);
    line-height: 23px;
  }
  .contact-list svg { width: 15px; height: 15px; fill: var(--ocean-deep); flex: none; }
  .address {
    position: absolute;
    right: 38px;
    top: 172px;
    text-align: right;
    font-size: 16px;
    line-height: 24px;
    font-style: normal;
    color: var(--ink);
  }
</style>
</head>
<body>
  <section class="card card-front">
    <div class="brand">
      <span class="brand-mark" role="img" aria-label="Tropical fish motif"></span>
      <span class="wordmark">Reef Lantern</span>
    </div>
    <div class="social-handle"><span class="dot"></span>@reeflantern</div>
  </section>

  <section class="card card-back">
    <div class="brand">
      <span class="brand-mark" role="img" aria-label="Tropical fish motif"></span>
      <span class="wordmark">Reef Lantern</span>
    </div>
    <div class="divider"></div>

    <div class="person">
      <div class="person-name">Nolan Brightwater</div>
      <div class="person-role">Managing Director</div>
      <ul class="contact-list">
        <li>
          <svg viewBox="0 0 16 16" aria-hidden="true"><path d="M3.6 1.5l2.2 2.6-1.3 1.6c.9 1.9 2.3 3.3 4.2 4.2l1.6-1.3 2.6 2.2-1.3 2.4C6.6 13 3 9.4 1.2 4.4z"/></svg>
          +15550142376
        </li>
        <li>
          <svg viewBox="0 0 16 16" aria-hidden="true"><path d="M1 3h14v10H1z M2 4.2v.4l6 4 6-4v-.4z" fill-rule="evenodd"/></svg>
          info@reeflantern.com
        </li>
        <li>
          <svg viewBox="0 0 16 16" aria-hidden="true"><path d="M8 1a7 7 0 1 0 0 14A7 7 0 0 0 8 1zm0 1.5c.9 0 1.8 1.9 2 4.5H6c.2-2.6 1.1-4.5 2-4.5zM2.6 7h2.2c.1-1.7.4-3.1 1-4A5.5 5.5 0 0 0 2.6 7zm0 2a5.5 5.5 0 0 0 3.2 4c-.6-.9-.9-2.3-1-4zm3.4 0c.2 2.6 1.1 4.5 2 4.5s1.8-1.9 2-4.5zm5.2 0c-.1 1.7-.4 3.1-1 4a5.5 5.5 0 0 0 3.2-4zm2.2-2a5.5 5.5 0 0 0-3.2-4c.6.9.9 2.3 1 4z"/></svg>
          www.reeflantern.com
        </li>
      </ul>
    </div>

    <address class="address">
      Reef Lantern Inc.<br>
      P.O Box 40210<br>
      Coral Bay, NV 89000
    </address>
  </section>
</body>
</html>
```